Gablestone Inspections Business Card

I need a business card for my new company. The company is going to provide home inspections. The name of the company is Gablestone Inspections. I am not sure if I want a single sided card or a double. I have a logo already that I want to incorporate into the card design. I was wondering if I should incorporate a catch phrase on my card or not. If I did the phrase would be "Careful Eyes on Every Corner of Your Home" but i am unsure how or if to use it on a card. The following information needs to be on the card.
Home Inspection
My Name: Tobias R. Fenwick Phone Number: 555-317-6420 Email: tfenwick@gablestoneinspections.com Website: www.gablestoneinspections.com NY HI License # 27300592415

```html
<!DOCTYPE html>
<html lang="en">
<head>
<meta charset="utf-8">
<title>Gablestone Inspections – Business Card</title>
<link href="https://fonts.googleapis.com/css2?family=Open+Sans:ital,wght@0,400;0,600;0,700;0,800;1,600&display=swap" rel="stylesheet">
<style>
  :root {
    --backdrop: #232323;
    --card-dark: #1f2125;
    --brand-blue: #1169ad;
    --brand-blue-bright: #1f7fcf;
    --ink-light: #ffffff;
  }
  * { box-sizing: border-box; margin: 0; padding: 0; }
  html, body {
    width: 1200px; height: 780px; overflow: hidden;
    background: var(--backdrop);
    font-family: "Open Sans", Arial, sans-serif;
  }
  .stage {
    position: relative; width: 1200px; height: 780px;
    display: flex; justify-content: center; align-items: center; gap: 60px;
  }
  .card {
    position: relative; width: 370px; height: 648px;
    border-radius: 30px; overflow: hidden;
    background: var(--card-dark);
    box-shadow: 0 18px 40px rgba(0,0,0,.55);
  }

  /* back side */
  .card-back .brand-vertical {
    position: absolute; left: 62px; bottom: 70px;
    transform-origin: left bottom; transform: rotate(-90deg) translate(0, 100%);
    display: flex; align-items: center; gap: 12px; white-space: nowrap;
  }
  .brand-mark-square {
    width: 18px; height: 18px; background: var(--brand-blue-bright); flex: none;
  }
  .brand-name {
    font-weight: 700; color: var(--brand-blue-bright);
    letter-spacing: .5px; white-space: nowrap;
  }
  .card-back .brand-name { font-size: 28px; }

  /* front side */
  .card-front .brand-top {
    position: absolute; top: 100px; left: 0; right: 0;
    display: flex; flex-direction: column; align-items: center; gap: 12px;
  }
  .card-front .brand-name { font-size: 27px; }
  .brand-rule { width: 230px; height: 2px; background: var(--brand-blue-bright); }

  .contact-band {
    position: absolute; left: 0; right: 0; bottom: 0; height: 340px;
    background: var(--brand-blue);
    color: var(--ink-light); text-align: center;
    padding-top: 36px;
  }
  .person-name { font-size: 31px; font-weight: 800; line-height: 1.1; }
  .person-role { font-size: 16px; font-weight: 600; font-style: italic; margin-top: 2px; }
  .contact-icons { display: flex; justify-content: center; gap: 10px; margin: 16px 0 10px; }
  .contact-icon {
    width: 28px; height: 28px; border-radius: 50%; background: var(--ink-light);
    display: flex; align-items: center; justify-content: center;
  }
  .contact-icon svg { width: 16px; height: 16px; }
  .contact-line { font-size: 15.5px; line-height: 1.45; }
  .contact-line.phone { font-size: 17px; }
  .divider { width: 110px; height: 2px; background: var(--ink-light); margin: 10px auto; }
  .license { font-size: 16px; }
  .tagline { font-size: 15.5px; }
</style>
</head>
<body>
<main class="stage">
  <section class="card card-back" aria-label="Card back">
    <div class="brand-vertical">
      <span class="brand-mark-square"></span>
      <span class="brand-name">Gablestone Inspections</span>
    </div>
  </section>

  <section class="card card-front" aria-label="Card front">
    <div class="brand-top">
      <span class="brand-name">Gablestone Inspections</span>
      <span class="brand-rule"></span>
    </div>

    <div class="contact-band">
      <h1 class="person-name">Tobias R. Fenwick</h1>
      <p class="person-role">Managing Director</p>
      <div class="contact-icons">
        <span class="contact-icon" aria-label="Phone">
          <svg viewBox="0 0 24 24"><path fill="#1169ad" d="M6.6 10.8a15 15 0 0 0 6.6 6.6l2.2-2.2c.3-.3.7-.4 1-.2 1.1.4 2.3.6 3.6.6.6 0 1 .4 1 1V20c0 .6-.4 1-1 1A17 17 0 0 1 3 4c0-.6.4-1 1-1h3.5c.6 0 1 .4 1 1 0 1.3.2 2.5.6 3.6.1.3 0 .7-.2 1z"/></svg>
        </span>
        <span class="contact-icon" aria-label="Email">
          <svg viewBox="0 0 24 24"><rect x="2" y="5" width="20" height="14" rx="2" fill="#1169ad"/><path d="M3 6l9 7 9-7" stroke="#fff" stroke-width="2" fill="none"/></svg>
        </span>
        <span class="contact-icon" aria-label="Website">
          <svg viewBox="0 0 24 24" fill="none" stroke="#1169ad" stroke-width="2"><circle cx="12" cy="12" r="9"/><ellipse cx="12" cy="12" rx="4" ry="9"/><path d="M3 12h18"/></svg>
        </span>
      </div>
      <p class="contact-line phone">555-317-6420</p>
      <p class="contact-line">www.gablestoneinspections.com</p>
      <p class="contact-line">tfenwick@gablestoneinspections.com</p>
      <div class="divider"></div>
      <p class="license">NY HI License # 27300592415</p>
      <div class="divider"></div>
      <p class="tagline">Careful Eyes on Every Corner of Your Home</p>
    </div>
  </section>
</main>
</body>
</html>
```